Business card design needed

I have a small café in a small coastal town on the Central coast of NSW (Aus) I need something simple but noticeable. My café is on the main rd and while there is a lot of passing traffic I need a logo which will make people notice us, either through pamphlets or signage. We make almost everything freshly on the premises including cakes, burgers, hot chips, coffees and milkshakes. we also sell some cake decorating supplies. I am pretty open to designs and don't mind if these items are incorporated in the design. My frontage is aqua and my outdoor furniture is beige. Inside we have a small amount of aqua and the walls are white. I am happy for any variations of these colours or anything which goes with the aqua.

Contact Information for Business Card

Reed & Lantern Café
127 Harrow Rd West Bindell
02 48 61 2593
Open for breakfast and lunch
from 6am Monday - Saturday

```html
<!DOCTYPE html>
<html lang="en">
<head>
<meta charset="utf-8">
<title>Reed &amp; Lantern Café – Business Card</title>
<link href="https://fonts.googleapis.com/css2?family=Alegreya:wght@400;700&display=swap" rel="stylesheet">
<style>
  :root {
    --backdrop: #e9e6e1;
    --card-aqua: #5faa9a;
    --card-aqua-deep: #569d8e;
    --cream: #f7dfc4;
    --beige: #e8c9a6;
  }
  * { margin: 0; padding: 0; box-sizing: border-box; }
  html, body {
    width: 1200px;
    height: 900px;
    overflow: hidden;
    background: var(--backdrop);
  }
  .stage {
    width: 1200px;
    height: 900px;
    display: flex;
    align-items: center;
    justify-content: center;
  }
  .business-card {
    width: 1000px;
    height: 572px;
    border-radius: 34px;
    background: radial-gradient(ellipse at 50% 40%, var(--card-aqua) 0%, var(--card-aqua-deep) 100%);
    box-shadow: 0 18px 40px rgba(0, 0, 0, 0.18);
    display: flex;
    flex-direction: column;
    align-items: center;
    font-family: "Alegreya", Georgia, serif;
    color: var(--cream);
    text-align: center;
  }
  .brand-mark {
    margin-top: 78px;
    width: 150px;
    height: 150px;
    border-radius: 50%;
    background: var(--beige);
  }
  .brand-name {
    margin-top: 34px;
    font-size: 50px;
    font-weight: 700;
    letter-spacing: 0.5px;
  }
  .contact-details {
    margin-top: 34px;
    font-size: 30px;
    font-weight: 400;
    line-height: 1.3;
  }
</style>
</head>
<body>
  <main class="stage">
    <article class="business-card">
      <div class="brand-mark" aria-hidden="true"></div>
      <h1 class="brand-name">Reed &amp; Lantern Café</h1>
      <p class="contact-details">
        127 Harrow Rd West Bindell - 02 48 61 2593 -<br>
        Open for breakfast and lunch from 6am Monday - Saturday
      </p>
    </article>
  </main>
</body>
</html>
```